Relocation/furniture installation company needs new business cards

we are a relocation and furniture installation company mainly dealing with corporate clients and we are looking for new business card ideas. Cards should incorporate our logo and list our website, phone number and services. The company is only 2 years old but with more staff joining we are in the need for more business cards, so something with an awesome design that is eye catching would go a long way to insure we get our name out there and look good to potential new clients.

Target Market(s)

Corporate

Industry/Entity Type

Trade

Contact Information for Business Card

www.merovanta.co.nz
0508 7 kelpor

furniture installation
business relocations
joinery installation
commercial property maintenance

Colors
0592cd
34a7d8
85cae6
85acd3
0356a4
cfdfed
cee9f5
757575
474747

Requirements
Must have
• Business relocations and furniture installation specialists
Nice to have
• something that incorporates our logo.

```html
<!DOCTYPE html>
<html lang="en">
<head>
<meta charset="utf-8">
<title>Merovanta business cards</title>
<link rel="stylesheet" href="https://fonts.googleapis.com/css2?family=Saira:wght@600;700&family=Open+Sans:wght@400&family=Roboto+Condensed:wght@400&display=swap">
<style>
  :root {
    --backdrop: #686868;
    --card: #f7f7f5;
    --navy: #2e3a8f;
    --azure: #0592cd;
    --sky: #00c4f4;
    --steel: #3a6aa3;
  }
  * { margin: 0; padding: 0; box-sizing: border-box; }
  html, body { width: 1200px; height: 1011px; overflow: hidden; background: var(--backdrop); }
  .card {
    position: absolute; left: 357px; width: 486px; height: 293px;
    background: var(--card); overflow: hidden;
  }
  .card-front { top: 186px; }
  .card-back { top: 532px; }

  .brand-name {
    position: absolute; font-family: "Saira", sans-serif; font-weight: 700;
    color: var(--navy); letter-spacing: 3px; white-space: nowrap;
  }
  .card-front .brand-name { left: 0; right: 0; top: 118px; text-align: center; font-size: 40px; }
  .brand-mark {
    display: inline-block; width: 14px; height: 14px; background: var(--azure);
    margin-right: 12px; vertical-align: middle; position: relative; top: -4px;
  }
  .front-web {
    position: absolute; left: 0; right: 0; top: 260px; height: 20px;
  }
  .front-web svg { position: absolute; left: 0; top: 0; }
  .front-web .url {
    position: absolute; left: 0; right: 0; top: 1px; text-align: center;
    font-family: "Open Sans", sans-serif; font-size: 12px; letter-spacing: 2.6px; color: var(--navy);
  }
  .front-web .url em { font-style: normal; color: var(--azure); }

  .card-back .brand-name { left: 20px; width: 210px; top: 118px; text-align: center; font-size: 28px; letter-spacing: 2px; }
  .divider {
    position: absolute; left: 245px; top: 56px; width: 1px; height: 164px;
    background: linear-gradient(var(--card), var(--azure), var(--card));
  }
  .person-name {
    position: absolute; left: 276px; top: 90px; font-family: "Saira", sans-serif; font-weight: 700;
    font-size: 25px; letter-spacing: 1.5px; color: var(--navy);
  }
  .contact-list { position: absolute; left: 276px; top: 130px; list-style: none; }
  .contact-list li {
    display: flex; align-items: center; height: 19.5px;
    font-family: "Open Sans", sans-serif; font-size: 13px; color: var(--navy);
  }
  .contact-list svg { width: 11px; height: 11px; margin-right: 10px; flex: none; }
  .band-base { position: absolute; left: 0; top: 274px; width: 240px; height: 19px; background: var(--navy); }
  .band-accent { position: absolute; left: 0; top: 0; }
  .tagline {
    position: absolute; left: 276px; top: 267px; font-family: "Roboto Condensed", sans-serif;
    font-size: 12px; color: #fff;
  }
</style>
</head>
<body>
  <section class="card card-front">
    <div class="brand-name"><span class="brand-mark"></span>MEROVANTA</div>
    <div class="front-web">
      <svg width="486" height="20" viewBox="0 0 486 20">
        <polygon points="30,10 146,7 146,12" fill="var(--navy)"/>
        <polygon points="456,10 340,7 340,12" fill="var(--navy)"/>
      </svg>
      <div class="url">www.<em>merovanta</em>.co.nz</div>
    </div>
  </section>

  <section class="card card-back">
    <div class="brand-name"><span class="brand-mark"></span>MEROVANTA</div>
    <div class="divider"></div>
    <div class="person-name">AARON HALE</div>
    <ul class="contact-list">
      <li><svg viewBox="0 0 12 12"><path d="M1 4c0-2 10-2 10 0v1H8V4H4v1H1z M3 6h6l2 5H1z" fill="var(--azure)"/></svg>0508 7 kelpor</li>
      <li><svg viewBox="0 0 12 12"><rect x="0.5" y="2" width="11" height="8" fill="var(--azure)"/><path d="M0.5 2L6 7l5.5-5" stroke="#fff" fill="none"/></svg>aaron@merovanta.co.nz</li>
      <li><svg viewBox="0 0 12 12"><circle cx="6" cy="6" r="5" fill="none" stroke="var(--azure)" stroke-width="1.2"/><path d="M1 6h10M6 1v10M3.5 2.5q-1.5 3.5 0 7M8.5 2.5q1.5 3.5 0 7" stroke="var(--azure)" fill="none" stroke-width="0.9"/></svg>www.merovanta.co.nz</li>
    </ul>
    <div class="band-base"></div>
    <svg class="band-accent" width="486" height="293" viewBox="0 0 486 293">
      <defs>
        <linearGradient id="accentFade" x1="0" y1="0" x2="1" y2="0">
          <stop offset="0" stop-color="var(--steel)"/>
          <stop offset="1" stop-color="var(--sky)"/>
        </linearGradient>
      </defs>
      <polygon points="251,255 486,255 486,293 226,293" fill="url(#accentFade)"/>
    </svg>
    <div class="tagline">Relocation and Furniture Installation</div>
  </section>
</body>
</html>
```